Commercial painting company is looking for a creative website designer.

Hi, we just completed our logo project and now ready to launch our website. The project will be done on Squarespace platform. It will contain:
Page 1 HOME
Page 2 SERVICES
Page 3 PICTURES
The content will be written by us. I am not sure bout the pictures, I do not have any to provide. I can buy stock photos if needed.
We are commercial only painting company and have to appeal to commercial, industrial property mangers. We will need CALL, REQUEST FOR ESTIMATE buttons.
If possible to have a live picture on home page would be great. Thank you
Target Market(s)
Property Managers
Industry/Entity Type
Commercial Painting
Other font styles liked:
- Poppins

```html
<!DOCTYPE html>
<html lang="en">
<head>
<meta charset="utf-8">
<title>Stripeline Painters – Commercial Painting</title>
<link href="https://fonts.googleapis.com/css2?family=Oswald:wght@500;600;700&family=Poppins:wght@400;500;600;700&display=swap" rel="stylesheet">
<style>
:root{
  --red:#e0193f;
  --red-deep:#c4102f;
  --navy:#1a2d6b;
  --navy-deep:#152458;
  --white:#ffffff;
  --ink:#333a4d;
  --muted:#6b7080;
  --field:#ededed;
  --pale:#d5dbe8;
}
*{margin:0;padding:0;box-sizing:border-box}
html,body{width:1200px;height:3840px;overflow:hidden;background:var(--white)}
body{position:relative;font-family:'Poppins',sans-serif;color:var(--ink)}
.abs{position:absolute}
.head{font-family:'Oswald',sans-serif;font-weight:600;text-transform:uppercase;line-height:1}
.center{left:0;width:1200px;text-align:center}

/* hero */
.hero-red{left:0;top:0;width:1200px;height:900px;background:linear-gradient(120deg,#f01e45,#d4123a 60%,#c40f33)}
.hero-photo{left:460px;top:80px;width:740px;height:720px;background:linear-gradient(160deg,#e8e8e8 0%,#c9c9c9 40%,#d43a58 80%);opacity:.9;clip-path:polygon(15% 0,100% 0,100% 78%,30% 100%,0 100%)}
.brand{left:90px;top:18px;display:flex;align-items:center;gap:10px;font-family:'Poppins',sans-serif;font-weight:700;font-size:17px;color:var(--white)}
.brand-dot{width:54px;height:54px;border-radius:50%;background:var(--white)}
.nav{top:38px;left:486px;display:flex;gap:25px;font-weight:600;font-size:14px;color:var(--white)}
.btn-call{left:738px;top:30px;width:172px;height:36px;border:2px solid var(--white);transform:skewX(-18deg);color:var(--white);font-size:11px;font-weight:700;display:flex;align-items:center;justify-content:center}
.btn-call span,.btn-est span,.btn-hero span{transform:skewX(18deg)}
.btn-est{left:916px;top:30px;width:190px;height:36px;background:var(--white);transform:skewX(-18deg);color:var(--navy);font-size:11px;font-weight:700;display:flex;align-items:center;justify-content:center}
.hero-title{left:84px;top:258px;font-size:102px;color:var(--white);font-weight:700;line-height:.97}
.hero-sub{left:85px;top:470px;font-family:'Oswald',sans-serif;font-size:35px;color:var(--white);font-weight:500}
.btn-hero{left:95px;top:532px;width:185px;height:38px;background:var(--white);transform:skewX(-18deg);color:var(--navy);font-size:11px;font-weight:700;display:flex;align-items:center;justify-content:center}
.play{left:966px;top:603px;width:144px;height:144px;border-radius:50%;background:var(--white);box-shadow:0 8px 20px rgba(0,0,0,.25);display:flex;align-items:center;justify-content:center}

/* sections */
.h2-light{color:var(--white);font-size:46px}
.h2-dark{color:var(--navy);font-size:48px}
.lead{font-size:13.5px;line-height:22px}
.card{width:303px;height:312px;clip-path:polygon(0 0,100% 0,100% 82%,0 100%)}
.card-label{left:26px;top:245px;font-family:'Oswald',sans-serif;font-weight:500;font-size:18px;color:var(--white)}
.feature-title{font-family:'Oswald',sans-serif;font-weight:500;font-size:19px;color:var(--navy);text-transform:uppercase}
.feature-text{font-size:13px;line-height:20px;color:var(--ink);width:345px;margin-top:6px}
.tile{width:246px;height:246px}
.field{left:227px;top:2953px;width:616px;height:57px;background:var(--field);display:flex;align-items:center;padding-left:32px;gap:12px;font-size:14px;color:var(--muted)}
.btn-sign{left:852px;top:2953px;width:156px;height:57px;background:var(--navy-deep);color:var(--white);font-weight:700;font-size:15px;display:flex;align-items:center;justify-content:center}
.notice{left:90px;top:3142px;width:1022px;height:230px;background:var(--red-deep);clip-path:polygon(0 0,100% 0,87% 100%,0 100%)}
.foot-h{font-family:'Oswald',sans-serif;font-weight:500;font-size:19px;color:var(--white);text-transform:uppercase}
.foot-list{font-size:12.5px;line-height:27px;color:var(--white)}
.foot-text{font-size:12.5px;line-height:18px;color:var(--white)}
.social{width:36px;height:36px;border-radius:50%;background:rgba(255,255,255,.15)}
</style>
</head>
<body>

<!-- hero -->
<div class="abs hero-red"></div>
<div class="abs hero-photo" role="img" aria-label="Painter in white cap and overalls rolling red paint onto a wall"></div>
<svg class="abs" style="left:0;top:560px" width="1200" height="1000" viewBox="0 0 1200 1000">
  <polygon fill="#1a2d6b" points="0,220 120,180 300,200 470,170 620,150 760,110 900,90 1050,60 1200,40 1200,940 900,900 600,860 300,820 0,780"/>
  <polygon fill="#d5dbe8" points="0,740 300,790 600,830 900,870 1200,900 1200,960 0,800"/>
</svg>
<div class="abs brand"><span class="brand-dot"></span>Stripeline Painters</div>
<nav class="abs nav"><span>HOME</span><span>SERVICES</span><span>GALLERY</span></nav>
<div class="abs btn-call"><span>CALL US: 123-456-789</span></div>
<div class="abs btn-est"><span>REQUEST FOR ESTIMATE</span></div>
<h1 class="abs head hero-title">Commercial<br>Painting</h1>
<div class="abs hero-sub">PAINTING HOUSE IS OUR PASSION</div>
<div class="abs btn-hero"><span>REQUEST FOR ESTIMATE</span></div>
<div class="abs play"><svg width="26" height="28" viewBox="0 0 26 28"><polygon points="4,2 24,14 4,26" fill="#e0193f"/></svg></div>

<!-- welcome -->
<h2 class="abs head center h2-light" style="top:862px">Welcome</h2>
<p class="abs lead" style="left:270px;top:925px;width:660px;text-align:center;color:var(--white)">Aenean sollicitudin, lorem quis bibendum auctor, nisi elit consequat ipsum, nec sagittis sem nibh uis sed odio sit amet nibh vulputate cursus a sit amet mauris. Morbi accumsan ipsum velit. Nam nec tellus a odio tincidunt auctor a ornare odio sed non....</p>
<div class="abs" style="left:90px;top:1050px;width:1020px;height:1px;background:rgba(255,255,255,.25)"></div>

<!-- services -->
<h2 class="abs head center h2-light" style="top:1095px">Our Services</h2>
<div class="abs card" style="left:130px;top:1170px;background:linear-gradient(160deg,#f2c200,#3b6fa0)" role="img" aria-label="Industrial painters in hard hats on a lift">
  <div class="abs card-label">INDUSTRY</div></div>
<div class="abs card" style="left:449px;top:1170px;background:linear-gradient(160deg,#5aa35a,#8c8c8c)" role="img" aria-label="Two painters rolling a green commercial wall">
  <div class="abs card-label">COMMERCIAL</div></div>
<div class="abs card" style="left:768px;top:1170px;background:linear-gradient(160deg,#6fc8d0,#2f5b8a)" role="img" aria-label="Painter rolling a teal interior wall">
  <div class="abs card-label">RESIDENTIAL</div></div>

<!-- customer service -->
<h2 class="abs head center h2-dark" style="top:1575px">Fast and Friendly Customer Service</h2>
<div class="abs" style="left:130px;top:1640px;width:500px;height:455px;background:radial-gradient(circle at 55% 50%,#d9dbe2,#f4f4f6 70%,#fff)" role="img" aria-label="Painter on a ladder with a roller beside paint cans"></div>

<svg class="abs" style="left:678px;top:1705px" width="56" height="56" viewBox="0 0 56 56" fill="none" stroke="#e0193f" stroke-width="2"><circle cx="28" cy="12" r="8"/><path d="M12 40 q16-22 32 0"/><polygon points="14,38 17,45 24,46 19,50 20,56 14,53 8,56 9,50 4,46 11,45"/><polygon points="42,38 45,45 52,46 47,50 48,56 42,53 36,56 37,50 32,46 39,45"/></svg>
<div class="abs" style="left:752px;top:1705px"><div class="feature-title">Experienced Technicians</div><div class="feature-text">Aenean sollicitudin, lorem quis bibendum auctor, nisi elit consequat ipsum, nec sagittis sem nibh id elit duis sed odio sit amet.</div></div>

<svg class="abs" style="left:682px;top:1822px" width="54" height="58" viewBox="0 0 54 58" fill="none" stroke="#e0193f" stroke-width="2"><rect x="2" y="6" width="36" height="48" rx="2"/><rect x="12" y="2" width="16" height="8"/><rect x="8" y="16" width="6" height="6"/><rect x="8" y="28" width="6" height="6"/><line x1="18" y1="19" x2="32" y2="19"/><line x1="18" y1="31" x2="30" y2="31"/><circle cx="42" cy="44" r="10"/><text x="38" y="49" font-size="13" fill="#e0193f" stroke="none">$</text></svg>
<div class="abs" style="left:752px;top:1820px"><div class="feature-title">Competitive Pricing</div><div class="feature-text">Aenean sollicitudin, lorem quis bibendum auctor, nisi elit consequat ipsum, nec sagittis sem nibh id elit duis sed odio sit amet.</div></div>

<svg class="abs" style="left:678px;top:1940px" width="56" height="58" viewBox="0 0 56 58" fill="none" stroke="#e0193f" stroke-width="2"><rect x="8" y="12" width="36" height="44" rx="2"/><path d="M4 14 l12-10 l8 6 l8-6 l12 10"/><path d="M16 30 l6 6 l14-14"/><line x1="14" y1="48" x2="38" y2="48"/></svg>
<div class="abs" style="left:752px;top:1938px"><div class="feature-title">Our Quality Promise</div><div class="feature-text">Aenean sollicitudin, lorem quis bibendum auctor, nisi elit consequat ipsum, nec sagittis sem nibh id elit duis sed odio sit amet.</div></div>

<!-- gallery -->
<h2 class="abs head center h2-dark" style="top:2165px">Our Gallery</h2>
<div class="abs tile" style="left:95px;top:2235px;background:linear-gradient(160deg,#dfe6ee,#2c5a8c)" role="img" aria-label="Rope-access painter on a building facade"></div>
<div class="abs tile" style="left:349px;top:2235px;background:linear-gradient(160deg,#f3d64a,#e9ecef 70%)" role="img" aria-label="Painter rolling yellow paint on a wall"></div>
<div class="abs tile" style="left:603px;top:2235px;background:linear-gradient(160deg,#c9cfd6,#e0a030 60%,#5a6a80)" role="img" aria-label="Painter hanging from ropes beside windows"></div>
<div class="abs tile" style="left:857px;top:2235px;background:linear-gradient(110deg,#e8eaec 40%,#f0c420)" role="img" aria-label="Painter in orange trousers painting a yellow wall"></div>
<div class="abs tile" style="left:95px;top:2488px;background:linear-gradient(160deg,#d9dde3,#c8443f 70%,#2f7ed8)" role="img" aria-label="Painter with a roller and blue bucket"></div>
<div class="abs tile" style="left:349px;top:2488px;background:linear-gradient(160deg,#e9e9e9,#8a8d92)" role="img" aria-label="Smiling painter in an orange hard hat holding a roller"></div>
<div class="abs tile" style="left:603px;top:2488px;background:#d0344f" role="img" aria-label="Painters at work, highlighted gallery item">
  <div class="abs" style="left:94px;top:94px;width:58px;height:58px;border-radius:50%;background:var(--white);display:flex;align-items:center;justify-content:center"><svg width="22" height="22" viewBox="0 0 22 22" fill="none" stroke="#1a2d6b" stroke-width="2.5"><circle cx="9" cy="9" r="6.5"/><line x1="14" y1="14" x2="20" y2="20"/></svg></div></div>
<div class="abs tile" style="left:857px;top:2488px;background:linear-gradient(160deg,#b8d4ee,#2f88d8 60%,#e8e4d8)" role="img" aria-label="Painter in a blue cap painting a window frame"></div>

<!-- newsletter -->
<h2 class="abs head center h2-dark" style="top:2855px">Stay Up To Date With</h2>
<p class="abs center" style="top:2912px;font-size:12.5px;color:var(--muted)">Interested in becoming a Fast Friendly? Please email become a supplier@example.com.</p>
<div class="abs field"><svg width="18" height="14" viewBox="0 0 18 14"><rect width="18" height="14" rx="2" fill="#b8bcc6"/><path d="M1 2 l8 6 l8-6" stroke="#ededed" stroke-width="1.5" fill="none"/></svg>Enter your email address</div>
<div class="abs btn-sign">SIGN UP</div>

<!-- special notice -->
<div class="abs" style="left:48px;top:3105px;width:122px;height:120px;background:rgba(26,45,107,.25)" role="img" aria-label="Decorative dot grid"></div>
<svg class="abs" style="left:0;top:3230px" width="1200" height="610" viewBox="0 0 1200 610">
  <polygon fill="#1a2d6b" points="0,260 200,200 400,170 600,150 800,140 1000,60 1200,10 1200,610 0,610"/>
</svg>
<div class="abs notice"></div>
<div class="abs head" style="left:182px;top:3218px;font-size:48px;color:var(--white)">Special Notice</div>
<div class="abs head" style="left:183px;top:3272px;font-size:16px;color:var(--white);font-weight:500">We are open for business!</div>
<div class="abs" style="left:525px;top:3200px;width:2px;height:105px;background:rgba(255,255,255,.5)"></div>
<p class="abs" style="left:572px;top:3222px;width:345px;font-size:13px;line-height:22px;color:var(--white)">Aenean sollicitudin, lorem quis bibendum auctor, nisi elit consequat ipsum, nec sagittis sem nibh id elit. Duis sed odio sit amet nibh vulputate</p>

<!-- footer -->
<div class="abs" style="left:120px;top:3520px;width:190px;height:190px;border-radius:50%;background:var(--white);display:flex;align-items:center;justify-content:center;text-align:center;font-weight:700;font-size:19px;color:var(--navy);line-height:1.3">Stripeline<br>Painters</div>
<div class="abs" style="left:382px;top:3492px"><div class="foot-h">Quick Links</div>
  <div class="foot-list" style="margin-top:18px">Home<br>Residential<br>Commercial<br>Portfolio<br>About<br>Contact Us</div></div>
<div class="abs" style="left:570px;top:3492px"><div class="foot-h">Contact Info</div>
  <div class="foot-text" style="margin-top:22px;padding-left:22px;position:relative"><svg style="position:absolute;left:0;top:3px" width="13" height="10" viewBox="0 0 13 10"><rect width="13" height="10" rx="1" fill="#fff"/></svg>Email:<br>info@example.com</div>
  <div class="foot-text" style="margin-top:16px;padding-left:22px;position:relative"><svg style="position:absolute;left:0;top:2px" width="13" height="13" viewBox="0 0 13 13"><path d="M2 1 l3 0 l1 3 l-2 1.5 q1.5 3 4 4 l1.5-2 l3 1 l0 3 q-8 0-12-11z" fill="#fff"/></svg>Phone:<br>123-456-7890</div>
  <div class="foot-text" style="margin-top:16px;padding-left:22px;position:relative"><svg style="position:absolute;left:0;top:2px" width="12" height="15" viewBox="0 0 12 15"><path d="M6 0 a6 6 0 0 1 6 6 c0 4-6 9-6 9 s-6-5-6-9 a6 6 0 0 1 6-6z" fill="#fff"/><circle cx="6" cy="6" r="2" fill="#1a2d6b"/></svg>Location:<br>Some address line goes<br>here city name</div></div>
<div class="abs" style="left:818px;top:3492px;width:250px"><div class="foot-h">Newsletter</div>
  <div class="foot-text" style="margin-top:20px">Join our mailing list to learn about our latest projects and product offerings</div>
  <div style="margin-top:22px;height:46px;background:var(--white);display:flex;align-items:center;justify-content:space-between;padding:0 14px;font-size:12px;color:var(--muted)"><span>✉ Enter your email...</span><svg width="16" height="16" viewBox="0 0 16 16"><polygon points="0,7 16,0 10,16 7,9" fill="#e0193f"/></svg></div>
  <div style="margin-top:30px;display:flex;gap:8px"><span class="social"></span><span class="social"></span><span class="social"></span><span class="social"></span></div></div>
<div class="abs" style="left:90px;top:3785px;width:1020px;height:1px;background:rgba(255,255,255,.2)"></div>
<div class="abs center" style="top:3810px;font-size:12px;font-weight:600;color:var(--white)">©2023 All Rights Reserved. TERMS &amp; CONDITIONS</div>
<div class="abs" style="left:1131px;top:3756px;width:44px;height:44px;border-radius:50%;background:var(--red);display:flex;align-items:center;justify-content:center"><svg width="12" height="14" viewBox="0 0 12 14" fill="none" stroke="#fff" stroke-width="1.6"><path d="M6 13 V2 M1 6 l5-5 l5 5"/></svg></div>

</body>
</html>
```